Hip / Cool Business Card for Custom Accessory Company

I would like to get a 2 sided design for standard size business cards, glossy (2 inches x 3.5 inches). Can be landscape or portrait layout! The design should include our logo (attached). The card should be extremely clear that the company is Tin Lantern. Should also have our URL clear. Should also use the color scheme seen on our upcoming site, tinlantern.example. The font we use is called "hurry up." Other than that, please go-to-town. We are targeting 15-45 y.o. market, with a skew on the 20-30 crowd. We do custom and stock iPhone cases as well as Cufflinks, Winestoppers; see the website for more.
Updates

Project Deadline Extended
Reason: Extending in case the US July 4th Holiday is keeping people from working!!

Industry/Entity Type

Landscape

Requirements
Must have
• Must be clear that the website is tinlantern.example. Must be clear that custom designs are an option.
Nice to have
• images of our designs. examples of our designs.
Should not have
• hard on the eyes contrasting colors such as orange on black. green on blue. Should not have any fonts that are considered "old" like Times New Roman. But decorative fonts are fine.

```html
<!DOCTYPE html>
<html lang="en">
<head>
<meta charset="utf-8">
<title>Tin Lantern – Business Card</title>
<link rel="stylesheet" href="https://fonts.googleapis.com/css2?family=Open+Sans:wght@400;600;700&display=swap">
<style>
  :root {
    --page-bg: #e9e9e7;
    --card-black: #262626;
    --card-black-deep: #1b1b1b;
    --brand-green: #4caf50;
    --brand-green-dark: #3a8f3e;
    --brand-green-light: #6cc36f;
    --brand-blue: #1565c0;
    --brand-blue-dark: #0f4f98;
    --brand-blue-light: #2f82d6;
    --brand-teal: #3fb3ad;
    --text-white: #ffffff;
    --text-muted: #bdbdbd;
    --text-dark: #1c1c1c;
    --card-shadow: 0 10px 28px rgba(0, 0, 0, 0.22);
  }

  * { box-sizing: border-box; margin: 0; padding: 0; }

  html, body {
    width: 1200px;
    height: 900px;
    overflow: hidden;
    background: var(--page-bg);
    font-family: "Open Sans", Arial, sans-serif;
  }

  .card-sheet {
    width: 1200px;
    height: 900px;
    display: flex;
    flex-direction: column;
    align-items: center;
    justify-content: center;
    gap: 60px;
  }

  .card {
    width: 620px;
    height: 354px;
    border-radius: 6px;
    overflow: hidden;
    box-shadow: var(--card-shadow);
    position: relative;
  }

  /* ---------- Back side ---------- */
  .card-back {
    background: var(--card-black);
    display: flex;
    flex-direction: column;
  }

  .card-back__brand {
    flex: 1 1 auto;
    display: flex;
    flex-direction: column;
    align-items: center;
    justify-content: center;
    gap: 12px;
  }

  .brand-dot {
    width: 58px;
    height: 58px;
    border-radius: 50%;
    background: #d9d9d9;
  }

  .brand-name {
    font-weight: 700;
    font-size: 40px;
    letter-spacing: 1px;
    text-transform: uppercase;
    color: var(--text-white);
    line-height: 1;
  }

  .brand-tagline {
    font-weight: 400;
    font-size: 15px;
    letter-spacing: 2px;
    text-transform: uppercase;
    color: var(--text-muted);
    line-height: 1;
  }

  .card-back__band {
    height: 100px;
    background: var(--brand-green);
    display: flex;
    align-items: center;
    justify-content: center;
  }

  .card-back__url {
    font-size: 28px;
    font-weight: 600;
    letter-spacing: 1px;
    color: var(--text-dark);
  }

  /* ---------- Front side ---------- */
  .card-front svg {
    display: block;
    width: 620px;
    height: 354px;
  }

  .front-brand {
    font-family: "Open Sans", Arial, sans-serif;
    font-weight: 700;
    font-size: 22px;
    fill: var(--text-dark);
    letter-spacing: 1px;
  }

  .front-name {
    font-family: "Open Sans", Arial, sans-serif;
    font-weight: 400;
    font-size: 25px;
    fill: var(--text-white);
  }

  .contact-label {
    font-family: "Open Sans", Arial, sans-serif;
    font-weight: 400;
    font-size: 13px;
    fill: var(--text-white);
  }
</style>
</head>
<body>
<main class="card-sheet">

  <!-- Back side -->
  <section class="card card-back" aria-label="Business card back">
    <div class="card-back__brand">
      <span class="brand-dot" aria-hidden="true"></span>
      <span class="brand-name">Tin Lantern</span>
      <span class="brand-tagline">Custom designs available</span>
    </div>
    <div class="card-back__band">
      <span class="card-back__url">www.tinlantern.example</span>
    </div>
  </section>

  <!-- Front side -->
  <section class="card card-front" aria-label="Business card front">
    <svg viewBox="0 0 560 320" xmlns="http://www.w3.org/2000/svg">
      <defs>
        <linearGradient id="blackPanel" x1="0" y1="0" x2="1" y2="1">
          <stop offset="0" stop-color="#333333"/>
          <stop offset="1" stop-color="#1b1b1b"/>
        </linearGradient>
      </defs>

      <!-- blue brand panel -->
      <rect class="panel-blue" width="560" height="320" fill="#1565c0"/>

      <!-- dark separator between blue and green -->
      <path class="curve-separator" d="M220 0 Q114 160 166 320 L560 320 L560 0 Z" fill="#1b1b1b"/>

      <!-- green curved stripe -->
      <path class="curve-green" d="M228 0 Q122 160 174 320 L560 320 L560 0 Z" fill="#4caf50"/>

      <!-- black info panel -->
      <path class="panel-black" d="M252 0 Q146 160 198 320 L560 320 L560 0 Z" fill="url(#blackPanel)"/>

      <!-- brand name with plain circle -->
      <circle class="brand-dot" cx="92" cy="134" r="30" fill="#3fb3ad"/>
      <text class="front-brand" x="92" y="200" text-anchor="middle">TIN</text>
      <text class="front-brand" x="92" y="228" text-anchor="middle">LANTERN</text>

      <!-- name & designation -->
      <text class="front-name" x="540" y="48" text-anchor="end">Name</text>
      <text class="front-name" x="540" y="78" text-anchor="end">designation</text>

      <!-- contact rows -->
      <g class="contact-row">
        <rect x="226" y="100" width="360" height="24" rx="12" fill="#4caf50"/>
        <rect x="226" y="124" width="340" height="8" fill="#3a8f3e"/>
        <circle cx="238" cy="112" r="11" fill="#6cc36f"/>
        <path d="M238 104 a5 5 0 0 1 5 5 c0 4 -5 9 -5 9 s-5 -5 -5 -9 a5 5 0 0 1 5 -5z" fill="#fff"/>
        <circle cx="238" cy="109" r="1.8" fill="#6cc36f"/>
        <text class="contact-label" x="254" y="117">Address</text>
      </g>

      <g class="contact-row">
        <rect x="212" y="142" width="380" height="24" rx="12" fill="#1565c0"/>
        <rect x="212" y="166" width="360" height="8" fill="#0f4f98"/>
        <circle cx="224" cy="154" r="11" fill="#2f82d6"/>
        <path d="M220 147 l3 -1 2 4 -2 2 c1 2 3 4 5 5 l2 -2 4 2 -1 3 c-6 0 -13 -7 -13 -13z" fill="#fff"/>
        <text class="contact-label" x="240" y="159">Mobile, Phone</text>
      </g>

      <g class="contact-row">
        <rect x="202" y="184" width="390" height="24" rx="12" fill="#4caf50"/>
        <rect x="202" y="208" width="370" height="8" fill="#3a8f3e"/>
        <circle cx="214" cy="196" r="11" fill="#6cc36f"/>
        <rect x="209" y="189" width="10" height="4" fill="#fff"/>
        <rect x="206" y="193" width="16" height="6" rx="1" fill="#fff"/>
        <rect x="209" y="199" width="10" height="4" fill="#fff"/>
        <text class="contact-label" x="230" y="201">Fax</text>
      </g>

      <g class="contact-row">
        <rect x="196" y="226" width="396" height="24" rx="12" fill="#1565c0"/>
        <rect x="196" y="250" width="376" height="8" fill="#0f4f98"/>
        <circle cx="208" cy="238" r="11" fill="#2f82d6"/>
        <rect x="201" y="233" width="14" height="10" fill="#fff"/>
        <path d="M201 233 l7 6 7 -6" fill="none" stroke="#2f82d6" stroke-width="1.3"/>
        <text class="contact-label" x="224" y="243">email</text>
      </g>

      <g class="contact-row">
        <rect x="194" y="268" width="398" height="24" rx="12" fill="#4caf50"/>
        <rect x="194" y="292" width="378" height="8" fill="#3a8f3e"/>
        <circle cx="206" cy="280" r="11" fill="#6cc36f"/>
        <g fill="none" stroke="#fff" stroke-width="1.3">
          <circle cx="206" cy="280" r="7"/>
          <ellipse cx="206" cy="280" rx="3" ry="7"/>
          <line x1="199" y1="280" x2="213" y2="280"/>
        </g>
        <text class="contact-label" x="222" y="285">website</text>
      </g>
    </svg>
  </section>

</main>
</body>
</html>
```